Want to market to schools to offer free chair massages for teacher and staff of the schools

This postcard will be mailed to all public schools in the U.S.

We want the schools to call our company to have a massage therapist provide free chair massages to the teachers and staff at their next School Improvement or Teacher Institute day.

want to make the postcard fun and inviting.

The postcard is 4 1/4" X 6"

FRONT AND BACK DESIGN.

For the back of postcard design, I have attached a template. You can use all the space except where the return label and stamp will go.

Target Market(s)

Target is schools and teachers

Industry/Entity Type

Teacher

```html
<!DOCTYPE html>
<html lang="en">
<head>
<meta charset="utf-8">
<title>Free Chair Massage Postcard</title>
<link rel="stylesheet" href="https://fonts.googleapis.com/css2?family=Arimo:wght@400;700&family=Cabin+Sketch:wght@700&family=Kalam:wght@700&display=swap">
<style>
  :root {
    --chalkboard: #3e7b4c;
    --chalkboard-dark: #2c5a37;
    --desk: #6b4a2a;
    --chalk: #f4f4f0;
    --ink: #1e1e1e;
    --accent-green: #3a8a36;
    --phone-green: #7bb646;
    --band-blue: #1b4fa1;
    --link-blue: #1a4ea2;
    --paper: #ffffff;
    --logo-navy: #1f3f8f;
  }
  * { margin: 0; padding: 0; box-sizing: border-box; }
  html, body { width: 1200px; height: 846px; overflow: hidden; background: var(--paper); }
  .postcard { position: relative; width: 1200px; height: 846px; background: var(--paper); font-family: "Arimo", Arial, sans-serif; color: var(--ink); }

  .hero-photo {
    position: absolute; left: 0; top: 0; width: 797px; height: 625px;
    background: linear-gradient(180deg, var(--chalkboard) 0%, var(--chalkboard-dark) 62%, var(--desk) 63%, #3a2a18 100%);
  }
  .headline { position: absolute; left: 183px; top: 28px; color: var(--chalk); }
  .headline-main { font-family: "Cabin Sketch", "Comic Sans MS", cursive; font-weight: 700; font-size: 100px; line-height: 84px; letter-spacing: 1px; }
  .headline-main span { display: block; }
  .headline-at { font-family: "Kalam", cursive; font-size: 40px; letter-spacing: 1px; }
  .headline-sub { font-family: "Kalam", cursive; font-weight: 700; font-size: 40px; line-height: 50px; letter-spacing: 1px; margin-top: 6px; margin-left: 10px; }

  .offer-copy { position: absolute; left: 830px; top: 34px; width: 350px; font-size: 23px; line-height: 29px; }
  .offer-copy p + p { margin-top: 12px; }
  .offer-thanks { margin-top: 40px !important; color: var(--accent-green); font-weight: 700; font-size: 25px; line-height: 33px; letter-spacing: 0.5px; }

  .cta-band { position: absolute; left: 0; top: 625px; width: 1200px; height: 59px; background: var(--band-blue); color: var(--paper); font-size: 36px; line-height: 59px; text-align: center; }
  .cta-band strong { font-weight: 700; }

  .contact { position: absolute; left: 60px; top: 700px; }
  .contact-phone { display: flex; align-items: center; gap: 10px; color: var(--phone-green); font-weight: 700; font-size: 64px; line-height: 72px; }
  .contact-web { margin-left: 102px; color: var(--link-blue); font-weight: 700; font-size: 30px; line-height: 40px; }

  .brand { position: absolute; left: 765px; top: 700px; display: flex; align-items: center; gap: 14px; }
  .brand-dot { width: 112px; height: 112px; border-radius: 50%; background: var(--logo-navy); }
  .brand-name { color: #444444; font-size: 38px; line-height: 42px; font-weight: 400; }
</style>
</head>
<body>
<main class="postcard">
  <div class="hero-photo" role="img" aria-label="Photo of a therapist giving a teacher a chair massage in front of a classroom chalkboard"></div>

  <h1 class="headline">
    <span class="headline-main"><span>FREE CHAIR</span><span>MASSAGE <span class="headline-at">AT YOUR</span></span></span>
    <span class="headline-sub">NEXT SCHOOL IMPROVEMENT<br>&amp; TEACHER INSTITUTE DAY</span>
  </h1>

  <section class="offer-copy">
    <p>Call to arrange complimentary chair massages with VitalCore Wellness Centers. We will send one of our affiliate therapists to your school and provide chair massages to Teachers and Staff.</p>
    <p>Massage helps relax tight and stiff muscles melting away stress. The therapist aims to release chronic stiffness in the neck and back.</p>
    <p class="offer-thanks">IT’S OUR WAY TO SHOW APPRECIATION TO THE TEACHERS</p>
  </section>

  <div class="cta-band"><strong>CALL TODAY</strong> TO RESERVE A DATE FOR YOUR <strong>SCHOOL</strong></div>

  <section class="contact">
    <div class="contact-phone">
      <svg width="40" height="52" viewBox="0 0 40 52" aria-hidden="true">
        <ellipse cx="20" cy="26" rx="17" ry="23" fill="none" stroke="currentColor" stroke-width="3"/>
        <path d="M15 13 q-6 13 0 26 l4-2 q-4-11 0-22 z" fill="currentColor"/>
      </svg>
      <span>1-800-555-0148</span>
    </div>
    <div class="contact-web">VitalCoreWellness.com</div>
  </section>

  <div class="brand">
    <span class="brand-dot" aria-hidden="true"></span>
    <span class="brand-name">VitalCore<br>Wellness Centers</span>
  </div>
</main>
</body>
</html>
```